Pebble Lantern Fine Chocolates
Handcrafted in Tucson, Arizona
Pebble Lantern Fine Chocolates -
Creative Brief
Customers who buy my chocolates or are interested in knowing more and purchasing them in the future. Foodies, Downtowners, Tucson tourists, students, coffee shop-types, mostly women.
they need to fit in a box that is 6 1/2 inches by 3 7/8 inches. Ideally, they will be approximately 4.5 inches by 13 3/4 inches, and then fold like an accordian 5 times to be 4.5 by 2 3/4 in your hand.

```html
<!DOCTYPE html>
<html lang="en">
<head>
<meta charset="utf-8">
<title>Pebble Lantern Fine Chocolates – Accordion Menu Card</title>
<link href="https://fonts.googleapis.com/css2?family=Great+Vibes&family=Cormorant+Garamond:ital,wght@0,600;1,500&display=swap" rel="stylesheet">
<style>
  :root {
    --page: #ffffff;
    --cocoa-deep: #2a0f06;
    --cocoa: #5a2a12;
    --cocoa-mid: #7a3d18;
    --gold-dark: #8a5a14;
    --gold: #c9962e;
    --gold-light: #f3d98a;
    --cream: #fff3d6;
    --ink-brown: #3b1a08;
    --cover-dark: #3a0505;
    --cover-mid: #8e1010;
  }
  * { box-sizing: border-box; margin: 0; padding: 0; }
  html, body {
    width: 1200px; height: 871px; overflow: hidden;
    background: var(--page);
  }
  .canvas { position: relative; width: 1200px; height: 871px; }
  .accordion-strip {
    position: absolute; left: 19px; top: 240px;
    width: 1162px; height: 389px;
    display: grid; grid-template-columns: repeat(5, 1fr);
    box-shadow: 0 2px 6px rgba(0,0,0,.25);
  }
  .flavor-panel {
    position: relative; overflow: hidden;
    background: linear-gradient(180deg, var(--cocoa-deep) 0%, var(--cocoa) 35%, var(--cocoa-mid) 56%, var(--gold) 60%, var(--gold-light) 78%, var(--gold) 100%);
    border-right: 1px solid var(--gold-dark);
  }
  .panel-frame {
    position: absolute; inset: 7px;
    border: 2px solid var(--gold);
    border-radius: 4px;
    box-shadow: inset 0 0 0 3px rgba(243,217,138,.35);
  }
  .panel-brand {
    position: absolute; left: 0; right: 0; top: 16px;
    text-align: center;
    font-family: "Cormorant Garamond", serif;
    font-weight: 600; font-size: 10px; letter-spacing: .04em;
    color: var(--gold-light);
  }
  .flavor-block { position: absolute; left: 22px; right: 22px; text-align: center; }
  .flavor-block.upper { top: 44px; }
  .flavor-block.lower { top: 246px; }
  .flavor-name {
    font-family: "Great Vibes", cursive;
    font-weight: 400;
    font-size: 17px; line-height: 1.1; margin-bottom: 5px;
  }
  .upper .flavor-name { color: var(--gold-light); }
  .lower .flavor-name { color: var(--ink-brown); }
  .flavor-note {
    font-family: "Cormorant Garamond", serif;
    font-style: italic; font-weight: 500;
    font-size: 8.5px; line-height: 1.3;
  }
  .upper .flavor-note { color: var(--cream); }
  .lower .flavor-note { color: var(--ink-brown); }
  .chocolate-photo {
    position: absolute; left: 42px; right: 42px; top: 148px; height: 82px;
    border-radius: 40%;
    background: radial-gradient(ellipse at 50% 45%, #a37a5e 0%, #6b3e25 45%, #3a1a0c 80%, rgba(58,26,12,0) 100%);
  }
  .brand-cover {
    position: relative; overflow: hidden;
    background: radial-gradient(ellipse at 50% 45%, var(--cover-mid) 0%, var(--cover-dark) 100%);
  }
  .brand-lockup {
    position: absolute; left: 0; right: 0; top: 50%; transform: translateY(-58%);
    display: flex; flex-direction: column; align-items: center; gap: 8px;
    text-align: center; padding: 0 24px;
  }
  .brand-dot {
    width: 14px; height: 14px; border-radius: 50%;
    background: var(--gold-light);
  }
  .brand-name {
    font-family: "Cormorant Garamond", serif;
    font-weight: 600; font-size: 18px; line-height: 1.15;
    color: var(--gold-light);
  }
</style>
</head>
<body>
<main class="canvas">
  <section class="accordion-strip">

    <article class="flavor-panel">
      <div class="panel-frame"></div>
      <p class="panel-brand">Pebble Lantern</p>
      <div class="flavor-block upper">
        <h2 class="flavor-name">Soft Mint</h2>
        <p class="flavor-note">Silky dark ganache with a gentle cool of fresh garden mint, rolled by hand in small batches and finished with a dusting of cocoa.</p>
      </div>
      <div class="chocolate-photo" role="img" aria-label="Photograph of assorted handmade chocolate truffles"></div>
      <div class="flavor-block lower">
        <h2 class="flavor-name">Le Bonbon</h2>
        <p class="flavor-note">Our house truffle of pure dark chocolate, whipped until airy and set by hand, the piece that started everything.</p>
      </div>
    </article>

    <article class="flavor-panel">
      <div class="panel-frame"></div>
      <p class="panel-brand">Pebble Lantern</p>
      <div class="flavor-block upper">
        <h2 class="flavor-name">Hazelnut Toffee</h2>
        <p class="flavor-note">Buttery toffee crunch folded with toasted hazelnuts and wrapped in milk chocolate for a warm, nutty bite that lingers.</p>
      </div>
      <div class="chocolate-photo" role="img" aria-label="Photograph of assorted handmade chocolate truffles"></div>
      <div class="flavor-block lower">
        <h2 class="flavor-name">Dark Chocolate Caramels</h2>
        <p class="flavor-note">Slow cooked caramel with a pinch of sea salt, enrobed in deep dark chocolate and chewy in all the best ways.</p>
      </div>
    </article>

    <article class="flavor-panel">
      <div class="panel-frame"></div>
      <p class="panel-brand">Pebble Lantern</p>
      <div class="flavor-block upper">
        <h2 class="flavor-name">Hazelnuts</h2>
        <p class="flavor-note">Whole roasted hazelnuts cradled in smooth praline and dipped in bittersweet chocolate, a simple classic made with desert patience.</p>
      </div>
      <div class="chocolate-photo" role="img" aria-label="Photograph of assorted handmade chocolate truffles"></div>
      <div class="flavor-block lower">
        <h2 class="flavor-name">Vanilla Mint with Lavender</h2>
        <p class="flavor-note">Madagascar vanilla and cool mint layered with a hint of lavender from local growers, calm and fragrant in every bite.</p>
      </div>
    </article>

    <article class="flavor-panel">
      <div class="panel-frame"></div>
      <p class="panel-brand">Pebble Lantern</p>
      <div class="flavor-block upper">
        <h2 class="flavor-name">Hibiscus and Raspberry</h2>
        <p class="flavor-note">Tart raspberry puree meets floral hibiscus tea in a bright pink ganache, sealed in a thin dark shell with a soft finish.</p>
      </div>
      <div class="chocolate-photo" role="img" aria-label="Photograph of assorted handmade chocolate truffles"></div>
      <div class="flavor-block lower">
        <h2 class="flavor-name">Tamarind Chili</h2>
        <p class="flavor-note">Sweet and sour tamarind with a quiet chili warmth, inspired by the markets of the borderlands and finished in dark chocolate.</p>
      </div>
    </article>

    <article class="brand-cover" role="img" aria-label="Red theatre curtain backdrop with a gold ribbon flourish">
      <div class="brand-lockup">
        <span class="brand-dot"></span>
        <h1 class="brand-name">Pebble Lantern Fine Chocolates</h1>
      </div>
    </article>

  </section>
</main>
</body>
</html>
```